Tenlo business card

I'm a hack at Illustrator, but have put together a set of business cards as attached. If someone could please improve these including good font selection, standard font sizes and spacing, nice layout and symmetry. Rear side the same on all cards. Basically make these cards into something impressive and professional.
Updates

Official logo just uploaded, please use these colours

Target Market(s)

50+ year old married couples

Industry/Entity Type

Business

Requirements
Must have
• Professional
Should not have
• Silly, cartoony

```html
<!DOCTYPE html>
<html lang="en">
<head>
<meta charset="utf-8">
<title>Tenlo business card</title>
<link href="https://fonts.googleapis.com/css2?family=Arimo:wght@400;700&display=swap" rel="stylesheet">
<style>
  :root {
    --teal: #17707c;
    --slate: #2f3d40;
    --ink: #333a3c;
    --paper: #ffffff;
    --backdrop: #e4e7e7;
    --muted: #d9e2e3;
  }
  * { margin: 0; padding: 0; box-sizing: border-box; }
  html, body { width: 1200px; height: 800px; overflow: hidden; }
  body {
    background: var(--backdrop);
    font-family: "Arimo", Arial, sans-serif;
    color: var(--ink);
  }
  .sheet {
    width: 1200px; height: 800px;
    display: flex; align-items: center; justify-content: center; gap: 40px;
  }
  .card {
    position: relative;
    width: 540px; height: 309px;
    box-shadow: 0 6px 18px rgba(0,0,0,0.18);
  }
  .card--front { background: var(--paper); }
  .card--back {
    background: var(--slate);
    display: flex; align-items: center; justify-content: center;
  }

  .brand {
    display: flex; align-items: center; gap: 10px;
    font-weight: 700; letter-spacing: 8px; text-transform: uppercase;
  }
  .brand__mark { width: 14px; height: 14px; }
  .card--front .brand {
    position: absolute; left: 40px; top: 80px;
    font-size: 30px; color: var(--teal);
  }
  .card--front .brand__mark { background: var(--teal); }
  .card--back .brand { font-size: 40px; color: var(--paper); }
  .card--back .brand__mark { background: var(--teal); width: 18px; height: 18px; }

  .person {
    position: absolute; right: 40px; top: 62px;
    text-align: right;
  }
  .person__name {
    font-size: 17px; font-weight: 700; color: var(--teal);
    letter-spacing: 0.5px; text-transform: uppercase;
  }
  .person__role { font-size: 12px; line-height: 15px; margin-top: 3px; }
  .person__rule {
    margin: 12px 0 0 auto; width: 190px; height: 2px; background: var(--teal);
  }

  .contact {
    position: absolute; right: 40px; bottom: 50px;
    text-align: right; font-size: 11.5px; line-height: 16px;
  }
  .contact__label { color: var(--teal); font-weight: 700; }
  .contact__small { font-size: 9.5px; }
</style>
</head>
<body>
  <main class="sheet">
    <section class="card card--front" aria-label="Front of card">
      <div class="brand"><span class="brand__mark"></span>Tenlo</div>

      <div class="person">
        <p class="person__name">Mark Dalton</p>
        <p class="person__role">General Manager</p>
        <p class="person__role">Building &amp; Technology Innovator</p>
        <div class="person__rule"></div>
      </div>

      <address class="contact" style="font-style: normal;">
        <p>14/56 Elm St, Fairview, VIC 3199, Australia · <span class="contact__label">T:</span> (+61) 03 5550 1040</p>
        <p><span class="contact__label">M:</span> 0400 555 123 · <span class="contact__label">D:</span> 03 5550 1088 · <span class="contact__label">E:</span> mark.dalton@tenlo.com.au</p>
        <p>www.tenlo.com.au · <span class="contact__small">REC 10458 &nbsp;ABN XXXXXXXXXXXXXX</span></p>
      </address>
    </section>

    <section class="card card--back" aria-label="Back of card">
      <div class="brand"><span class="brand__mark"></span>Tenlo</div>
    </section>
  </main>
</body>
</html>
```